Business card design needed for Automotive Reconditioning business

I have a logo design i just cant decide on the best color or layout for the business card, I will upload all the files so you can see all colors schemes we are considering. I have other file formats if needed let me know.

Target Market(s)

automotive dealerships

Contact Information for Business Card

HERE are the Descriptions and info needed on the card:
Interior Repair: Leather carpet burns panels dash Deoderize
Dealer products and Vin Verify
( spot for name and cell number) My name is Norman Bexley phone 614 352-4180 Title COO www.QuorvalMotive.com

Font styles to use
Sans Serif
Other font styles liked:
• what ever you think looks best

Requirements
Must have
• Must be able to change the name and phone for employees

```html
<!DOCTYPE html>
<html lang="en">
<head>
<meta charset="UTF-8">
<title>Quorval Motive – Business Card</title>
<link href="https://fonts.googleapis.com/css2?family=Montserrat:wght@300;400;600;700&display=swap" rel="stylesheet">
<style>
  :root {
    --stage: #2b3034;
    --card: #1c1c1c;
    --lime: #7cc428;
    --grey: #9b9b9b;
    --white: #f2f2f2;
  }
  html, body {
    margin: 0;
    padding: 0;
    width: 1200px;
    height: 900px;
    overflow: hidden;
    background: var(--stage);
    font-family: "Montserrat", sans-serif;
  }
  .business-card {
    position: absolute;
    left: 100px;
    top: 164px;
    width: 1000px;
    height: 572px;
    background: var(--card);
    border-radius: 6px;
    box-shadow: 0 20px 50px rgba(0,0,0,0.45);
  }
  .card-frame {
    position: absolute;
    inset: 30px;
    border: 2px solid var(--lime);
  }
  .contact {
    position: absolute;
    left: 150px;
    top: 62px;
  }
  .contact-name {
    margin: 0;
    font-size: 30px;
    font-weight: 600;
    color: var(--grey);
    letter-spacing: 1px;
  }
  .contact-title {
    margin: 2px 0 0;
    font-size: 22px;
    font-weight: 700;
    color: var(--lime);
  }
  .contact-phone {
    margin: 8px 0 0;
    font-size: 17px;
    font-weight: 600;
    color: var(--grey);
    letter-spacing: 2px;
  }
  .brand {
    position: absolute;
    left: 62px;
    top: 210px;
    display: flex;
    align-items: center;
    gap: 14px;
  }
  .brand-dot {
    width: 22px;
    height: 22px;
    border-radius: 50%;
    background: var(--lime);
  }
  .brand-name {
    font-size: 34px;
    font-weight: 700;
    color: var(--white);
    letter-spacing: 1px;
  }
  .services {
    position: absolute;
    left: 520px;
    top: 292px;
  }
  .services-heading {
    margin: 0 0 14px;
    font-size: 26px;
    font-weight: 300;
    color: var(--lime);
    letter-spacing: 3px;
    text-transform: uppercase;
  }
  .services-list {
    list-style: none;
    margin: 0;
    padding: 0;
  }
  .services-list li {
    font-size: 21px;
    font-weight: 400;
    color: var(--white);
    letter-spacing: 1.5px;
    line-height: 34px;
  }
  .website {
    position: absolute;
    left: 150px;
    top: 470px;
    margin: 0;
    font-size: 18px;
    font-weight: 600;
    color: var(--lime);
    letter-spacing: 1.5px;
  }
</style>
</head>
<body>
  <article class="business-card">
    <div class="card-frame"></div>

    <div class="contact">
      <p class="contact-name">Norman Bexley</p>
      <p class="contact-title">COO</p>
      <p class="contact-phone">614 352-4180</p>
    </div>

    <div class="brand">
      <span class="brand-dot"></span>
      <span class="brand-name">Quorval Motive</span>
    </div>

    <section class="services">
      <h2 class="services-heading">Interior Repair</h2>
      <ul class="services-list">
        <li>Leather carpet burns panels dash</li>
        <li>Deoderize</li>
        <li>Dealer products</li>
        <li>Vin Verify</li>
      </ul>
    </section>

    <p class="website">www.QuorvalMotive.com</p>
  </article>
</body>
</html>
```